Touch screen based web site design

We have a product called kVolt.

It is a browser based touch screen application for the apartment leasing industry . You can read more about it at http://kvolt.tarvelcorp.example.

To see how the product functions, you can check the link http://www.webkvolt.example/kvolt.aspx?k=demo1.

We have a need to give a new look and feel to the application. The redesign is NOT to be limited to colors and shapes, but an overhaul of the screen layout, color, font scheme to make the application flow nice and smooth. The content of the pages will remain the same.

There will be animations but that can be done by our IT team, if described in concept by the designer.

Again to reiterate, all things are up for grab, do not get influenced by the images, shapes and color used currently.
Updates

Project Deadline Extended
Reason: None of the design are coming even close to what I am asking for. Please see the homepage of the application at http://www.tarvelcorp.example/kvolt/images/img-screenshot-lg-01.jpg. That is what I am asking for as the first page to show the design idea.

Project Deadline Extended
Reason: At least the last couple of designs submitted understands it is a touch screen and the home page is not a web site home page. The reason I am still not able to select a design is that the quality of graphic design elements is sub par. For example, The treatment to the options for example are not sharp and up to mark.

Target Market(s)

Propective residents walking into a apartment leasing centers

Industry/Entity Type

Apartment

Requirements
Must have
• - Must have a design where the content, like name of the property, menu options and pictures, are dynamic. So for example, do not restrict the design in a manner that we cannot switch off an option without redesign of the page.
- Good use of icons for options
- Gives the user a calm and serene feeling while maintaining a crisp modern user interface
Nice to have
• - Design in a manner that the background can be a custom image for a specific client
- Description of animation on the screen where the images selected by the client can rotate/slide/appear/animate
Should not have
• - Boxy design
- Small options that cannot be touched by fingers
- dont plan on hover animations, will not work in touch

```html
<!DOCTYPE html>
<html lang="en">
<head>
<meta charset="utf-8">
<title>kVolt – Welcome</title>
<link rel="stylesheet" href="https://fonts.googleapis.com/css2?family=Baloo+2:wght@700&family=Signika:wght@500&family=Gochi+Hand&display=swap">
<style>
  :root {
    --leaf-light: #eaf6c9;
    --leaf-mid: #a8d96a;
    --leaf-deep: #5a9e2c;
    --band-white: rgba(255, 255, 255, 0.55);
    --band-line: rgba(255, 255, 255, 0.95);
    --ink: #1c1c1c;
    --accent-green: #1f7a12;
    --nav-green: #3f8f14;
    --ring: #e4e4e4;
    --button-edge: #d8d8d8;
    --people-icon: #4a78b8;
  }
  html, body {
    margin: 0;
    padding: 0;
    overflow: hidden;
  }
  .screen {
    position: relative;
    width: 1200px;
    height: 1043px;
    overflow: hidden;
    font-family: "Baloo 2", sans-serif;
  }
  .screen-backdrop {
    position: absolute;
    inset: 0;
    background:
      radial-gradient(ellipse 520px 380px at 160px 620px, rgba(255,255,255,0.75), transparent 70%),
      radial-gradient(ellipse 420px 300px at 1000px 180px, rgba(90,160,40,0.55), transparent 70%),
      radial-gradient(ellipse 380px 320px at 260px 300px, rgba(70,150,30,0.55), transparent 70%),
      radial-gradient(ellipse 400px 300px at 1050px 900px, rgba(80,150,30,0.5), transparent 70%),
      linear-gradient(160deg, var(--leaf-mid) 0%, var(--leaf-light) 45%, var(--leaf-mid) 80%, var(--leaf-deep) 100%);
  }
  .top-bar {
    position: absolute;
    left: 0; top: 0;
    width: 1200px;
    height: 127px;
    background: var(--band-white);
    border-bottom: 1px solid var(--band-line);
  }
  .property-name {
    position: absolute;
    left: 115px;
    top: 32px;
    margin: 0;
    font-size: 62px;
    font-weight: 700;
    line-height: 1;
    color: #2a2a2a;
    letter-spacing: 1px;
  }
  .tagline {
    position: absolute;
    right: 92px;
    top: 64px;
    margin: 0;
    font-size: 27.5px;
    font-weight: 700;
    line-height: 1.2;
    color: var(--ink);
    white-space: nowrap;
  }
  .tagline-accent { color: var(--accent-green); }
  .gallery {
    position: absolute;
    left: 0; top: 0;
  }
  .bottom-bar {
    position: absolute;
    left: 0; top: 914px;
    width: 1200px;
    height: 129px;
    background: var(--band-white);
  }
  .prompt {
    position: absolute;
    left: 94px;
    top: 942px;
    margin: 0;
    font-family: "Gochi Hand", cursive;
    font-size: 30px;
    line-height: 38px;
    color: #222;
    white-space: nowrap;
  }
  .prompt-line-2 { padding-left: 26px; }
  .prompt-arrow {
    position: absolute;
    left: 304px; top: 959px;
  }
  .menu {
    position: absolute;
    left: 0; top: 0;
    margin: 0; padding: 0;
    list-style: none;
  }
  .menu-option {
    position: absolute;
    width: 140px;
    text-align: center;
  }
  .menu-button {
    display: block;
    width: 132px; height: 132px;
    margin: 0 auto;
  }
  .menu-label {
    display: block;
    margin-top: 3px;
    font-family: "Signika", sans-serif;
    font-weight: 500;
    font-size: 17px;
    color: var(--nav-green);
    white-space: nowrap;
  }
</style>
</head>
<body>
<main class="screen">
  <div class="screen-backdrop" role="img" aria-label="Soft-focus photo of green maple leaves on sunlit branches"></div>

  <header class="top-bar">
    <h1 class="property-name">kVolt</h1>
    <p class="tagline">When your are here you <span class="tagline-accent">know you have arrived</span></p>
  </header>

  <svg class="gallery" width="1200" height="1043" viewBox="0 0 1200 1043">
    <defs>
      <linearGradient id="pool" x1="0" y1="0" x2="0" y2="1">
        <stop offset="0" stop-color="#9aa3ad"/><stop offset="0.5" stop-color="#8a6a5a"/><stop offset="0.65" stop-color="#3fb2e6"/><stop offset="1" stop-color="#b05a48"/>
      </linearGradient>
      <linearGradient id="yoga" x1="0" y1="0" x2="0" y2="1">
        <stop offset="0" stop-color="#fbf6f0"/><stop offset="0.6" stop-color="#efe2d2"/><stop offset="1" stop-color="#b5622f"/>
      </linearGradient>
      <linearGradient id="trail" x1="0" y1="0" x2="1" y2="1">
        <stop offset="0" stop-color="#e39a1c"/><stop offset="0.5" stop-color="#b86a1a"/><stop offset="0.8" stop-color="#8fb0c9"/><stop offset="1" stop-color="#5f7f3a"/>
      </linearGradient>
      <linearGradient id="kitchen" x1="0" y1="0" x2="0" y2="1">
        <stop offset="0" stop-color="#c9b7a0"/><stop offset="0.4" stop-color="#5a3520"/><stop offset="1" stop-color="#7d5535"/>
      </linearGradient>
      <linearGradient id="lake" x1="0" y1="0" x2="0" y2="1">
        <stop offset="0" stop-color="#e4e2f2"/><stop offset="0.35" stop-color="#8a8a6a"/><stop offset="0.5" stop-color="#3f6b3a"/><stop offset="0.7" stop-color="#7ca88a"/><stop offset="1" stop-color="#2f6a2a"/>
      </linearGradient>
      <radialGradient id="buttonFace" cx="0.5" cy="0.35" r="0.7">
        <stop offset="0" stop-color="#ffffff"/><stop offset="1" stop-color="#e6e6e6"/>
      </radialGradient>
    </defs>
    <g role="img" aria-label="Photo of the community pool with clubhouse and apartment buildings">
      <circle cx="540" cy="334" r="144" fill="var(--ring)"/>
      <circle cx="540" cy="334" r="131" fill="url(#pool)"/>
    </g>
    <g role="img" aria-label="Photo of a kitchen with dark wood cabinets and bar stools">
      <circle cx="540" cy="720" r="144" fill="var(--ring)"/>
      <circle cx="540" cy="720" r="131" fill="url(#kitchen)"/>
    </g>
    <g role="img" aria-label="Photo of a resident stretching in the fitness studio">
      <circle cx="724" cy="524" r="144" fill="var(--ring)"/>
      <circle cx="724" cy="524" r="131" fill="url(#yoga)"/>
    </g>
    <g role="img" aria-label="Photo of a cyclist on an autumn tree-lined trail">
      <circle cx="951" cy="392" r="144" fill="var(--ring)"/>
      <circle cx="951" cy="392" r="131" fill="url(#trail)"/>
    </g>
    <g role="img" aria-label="Photo of a lake with trees and snowy mountains">
      <circle cx="949" cy="683" r="144" fill="var(--ring)"/>
      <circle cx="949" cy="683" r="131" fill="url(#lake)"/>
    </g>
  </svg>

  <div class="bottom-bar"></div>

  <p class="prompt">Touch an option<br><span class="prompt-line-2">to explore</span></p>
  <svg class="prompt-arrow" width="52" height="44" viewBox="0 0 52 44" aria-hidden="true">
    <defs>
      <linearGradient id="arrowFill" x1="0" y1="0" x2="0" y2="1">
        <stop offset="0" stop-color="#b4f03c"/><stop offset="1" stop-color="#4fae0e"/>
      </linearGradient>
    </defs>
    <path d="M2 13 H26 V2 L50 22 L26 42 V31 H2 Z" fill="url(#arrowFill)"/>
  </svg>

  <ul class="menu">
    <li class="menu-option" style="left:403px; top:878px;">
      <svg class="menu-button" viewBox="0 0 132 132" aria-hidden="true">
        <circle cx="66" cy="66" r="64" fill="url(#buttonFace)" stroke="var(--button-edge)" stroke-width="2"/>
        <g fill="var(--people-icon)">
          <circle cx="38" cy="52" r="9"/>
          <path d="M22 86 Q23 66 38 66 Q53 66 54 86 Z"/>
          <circle cx="94" cy="52" r="9"/>
          <path d="M78 86 Q79 66 94 66 Q109 66 110 86 Z"/>
          <circle cx="66" cy="46" r="12"/>
          <path d="M44 94 Q46 64 66 64 Q86 64 88 94 Z"/>
        </g>
      </svg>
      <span class="menu-label">Community</span>
    </li>
    <li class="menu-option" style="left:581px; top:878px;">
      <svg class="menu-button" viewBox="0 0 132 132" aria-hidden="true">
        <circle cx="66" cy="66" r="64" fill="url(#buttonFace)" stroke="var(--button-edge)" stroke-width="2"/>
        <path d="M24 60 L56 32 L88 60 Z" fill="#555"/>
        <rect x="32" y="58" width="48" height="40" fill="#f2efe6" stroke="#888"/>
        <rect x="80" y="66" width="28" height="32" fill="#444"/>
        <path d="M76 66 L94 52 L112 66 Z" fill="#333"/>
        <rect x="38" y="66" width="12" height="10" fill="#7fb0d8"/>
        <rect x="60" y="66" width="12" height="10" fill="#7fb0d8"/>
        <rect x="50" y="80" width="12" height="18" fill="#c0692a"/>
      </svg>
      <span class="menu-label">Neighborhood</span>
    </li>
    <li class="menu-option" style="left:761px; top:878px;">
      <svg class="menu-button" viewBox="0 0 132 132" aria-hidden="true">
        <circle cx="66" cy="66" r="64" fill="url(#buttonFace)" stroke="var(--button-edge)" stroke-width="2"/>
        <rect x="26" y="32" width="82" height="70" fill="#fff" stroke="#bbb"/>
        <rect x="26" y="32" width="82" height="14" fill="#4c6fa8"/>
        <g stroke="#d2d2d2" stroke-width="1">
          <path d="M26 60 H108 M26 74 H108 M26 88 H108"/>
          <path d="M42 46 V102 M58 46 V102 M74 46 V102 M90 46 V102"/>
        </g>
        <rect x="58" y="60" width="16" height="14" fill="#f3c6c6"/>
      </svg>
      <span class="menu-label">Floor Plans</span>
    </li>
    <li class="menu-option" style="left:940px; top:878px;">
      <svg class="menu-button" viewBox="0 0 132 132" aria-hidden="true">
        <circle cx="66" cy="66" r="64" fill="url(#buttonFace)" stroke="var(--button-edge)" stroke-width="2"/>
        <rect x="24" y="38" width="84" height="58" rx="4" fill="#eef1f4" stroke="#a9b3bd"/>
        <rect x="34" y="50" width="24" height="28" fill="#5a8fc4"/>
        <rect x="66" y="48" width="9" height="7" fill="#4a6a90"/>
        <rect x="79" y="48" width="9" height="7" fill="#4a6a90"/>
        <rect x="92" y="48" width="9" height="7" fill="#4a6a90"/>
        <rect x="66" y="62" width="35" height="4" fill="#4a6a90"/>
        <rect x="66" y="71" width="35" height="4" fill="#4a6a90"/>
        <rect x="66" y="80" width="35" height="4" fill="#4a6a90"/>
        <rect x="30" y="98" width="72" height="6" fill="#c8ced4"/>
      </svg>
      <span class="menu-label">Contact</span>
    </li>
  </ul>
</main>
</body>
</html>
```